Webdesign für Metallbau-Wasserkraft Tessmar Lauber GmbH & Co. KG
Zielgruppe
Das Unternehmen ist im Metall- und Stahlwasserbau tätig. Die Haupkompetenz liegt im Stahlwasserbau, Rechenreinigung und Stahlbau tätig.
Aufgabenstellung
Die vorhandenen Seite https://www.metallbau-tessmar-lauber-beispiel.de/ soll einen Relaunch erhalten. Das Design soll frisch, modern und aussagekräftig erscheinen, trotz der Tradition und des Handwerksbetriebes.
Die Navigationstruktur soll erhalten bleiben. Hinzu kommt der Punkt 'Neuigkeiten'.

```html
<!DOCTYPE html>
<html lang="de">
<head>
<meta charset="utf-8">
<title>Metallbau-Wasserkraft Tessmar Lauber GmbH &amp; Co. KG</title>
<link rel="stylesheet" href="https://fonts.googleapis.com/css2?family=Oswald:wght@500&family=Open+Sans:wght@300;400;600&display=swap">
<style>
:root{
  --blue:#0a7db5;
  --blue-dark:#0b6596;
  --sky:#e1f3fb;
  --white:#ffffff;
  --text:#333a40;
  --muted:#555d63;
}
*{box-sizing:border-box;margin:0;padding:0}
html,body{width:1200px;height:2537px;overflow:hidden;background:var(--white)}
body{font-family:"Open Sans",Arial,sans-serif;color:var(--text)}
.page{position:relative;width:1219px;height:2576px;transform:scale(0.9845);transform-origin:0 0;overflow:hidden;background:var(--sky)}
.abs{position:absolute}
a{color:inherit;text-decoration:none}

.topbar{left:0;top:0;width:1219px;height:31px;background:var(--blue);color:var(--white);font-size:11px;font-weight:600;z-index:4}
.topbar .item{position:absolute;top:7px;display:flex;align-items:center;gap:9px}
.topbar .phone{left:478px;text-decoration:underline}
.topbar .mail{left:692px}

.header{left:0;top:31px;width:1219px;height:62px;background:var(--white);box-shadow:0 2px 6px rgba(0,0,0,.12);z-index:4}
.brand{position:absolute;left:52px;top:10px;display:flex;align-items:center;gap:10px}
.brand .mark{width:40px;height:40px;border:3px solid var(--blue)}
.brand .name{font-weight:600;color:var(--blue);font-size:12px;line-height:14px;width:200px}
.nav{position:absolute;right:192px;top:23px;display:flex;gap:33px;font-size:12px;color:var(--text)}

.hero{left:0;top:93px;width:1219px;height:440px;background:linear-gradient(180deg,#a9b7c3 0%,#7e8e7a 35%,#6f7a6a 55%,#3e5e70 80%,#2f5064 100%);z-index:1}
.hero h1{position:absolute;left:0;width:1219px;top:285px;text-align:center;font-family:"Oswald",sans-serif;font-weight:500;color:var(--white);font-size:44px;line-height:51px;text-shadow:0 2px 6px rgba(0,0,0,.4)}
.hero-wave{left:0;top:480px;z-index:2}

.intro{left:0;top:540px;width:1219px;height:640px;background:var(--sky)}
.h2{position:absolute;left:0;width:1219px;text-align:center;font-family:"Oswald",sans-serif;font-weight:500;color:var(--blue);font-size:32px}
.lead{position:absolute;left:0;width:1219px;top:110px;text-align:center;font-size:22px;font-weight:300;color:var(--text)}
.copy{position:absolute;left:191px;top:180px;width:405px;font-size:12.3px;line-height:19px;font-weight:300;color:var(--text)}
.ticks{list-style:none;margin:6px 0 4px;font-weight:400;font-size:12.5px}
.ticks li{display:flex;align-items:center;gap:6px;line-height:19px}
.btn{position:absolute;left:262px;width:195px;height:35px;border-radius:18px;background:var(--blue);color:var(--white);display:flex;align-items:center;box-shadow:0 3px 5px rgba(0,0,0,.2)}
.btn svg{margin-left:26px;margin-right:22px}
.btn.call{top:466px;font-size:15px}
.btn.send{top:517px;font-size:13px}
.photo-building{position:absolute;left:691px;top:180px;width:338px;height:400px;border-radius:6px;background:linear-gradient(160deg,#8ea07a 0%,#e3c77a 30%,#d9b86a 60%,#a8a8a8 85%,#eeeeee 100%)}

.products{left:0;top:1170px;width:1219px;height:630px;background:var(--white)}
.card{position:absolute;top:196px;width:267px;height:336px;background:var(--blue);border-radius:4px;color:var(--white)}
.card .badge{position:absolute;left:80px;top:-50px;width:108px;height:108px;border-radius:50%;background:var(--blue);border:6px solid var(--white);display:flex;align-items:center;justify-content:center}
.card h3{margin-top:80px;text-align:center;font-weight:300;font-size:24px}
.card ul{list-style:none;margin:17px 0 0 20px;font-size:16px;line-height:25.4px}
.card li::before{content:"»";margin-right:8px}

.news{left:0;top:1780px;width:1219px;height:640px;background:var(--sky)}
.post{position:absolute;top:125px;width:266px;height:353px;background:var(--white);border-radius:4px;overflow:hidden}
.post .pic{height:184px}
.post .date{margin:20px 0 0 19px;font-size:10px;color:var(--blue)}
.post h4{margin:8px 19px 0;font-weight:400;font-size:16px;line-height:21.5px;color:var(--text)}
.post p{margin:14px 19px 0;font-size:11px;line-height:18px;font-weight:300;color:var(--muted)}
.more{position:absolute;left:511px;top:518px;width:195px;height:35px;border-radius:18px;background:var(--white);color:var(--blue);font-weight:600;font-size:13px;display:flex;align-items:center;justify-content:center;box-shadow:0 3px 5px rgba(0,0,0,.2)}

.footer{left:0;top:2395px;width:1219px;height:135px;background:var(--blue);color:var(--white);font-size:12px;line-height:18px}
.footer .col{position:absolute;top:28px}
.footer .col svg{display:block;margin-bottom:6px}
.bottombar{left:0;top:2528px;width:1219px;height:48px;background:var(--blue-dark);color:#dcecf5;font-size:13px}
.bottombar nav{position:absolute;left:189px;top:14px;display:flex;gap:62px}
</style>
</head>
<body>
<div class="page">

  <div class="abs topbar">
    <span class="item phone">
      <svg width="16" height="16" viewBox="0 0 24 24" fill="none" stroke="#fff" stroke-width="1.6"><path d="M5 3h4l2 5-2.5 1.5a11 11 0 0 0 6 6L16 13l5 2v4a2 2 0 0 1-2 2A16 16 0 0 1 3 5a2 2 0 0 1 2-2z"/></svg>
      03746 558310</span>
    <span class="item mail">
      <svg width="18" height="14" viewBox="0 0 24 18" fill="none" stroke="#fff" stroke-width="1.6"><rect x="1" y="1" width="22" height="16" rx="3"/><path d="M2 3l10 7 10-7"/></svg>
      info@metallbau-tessmar-lauber-beispiel.de</span>
  </div>

  <header class="abs header">
    <div class="brand">
      <span class="mark"></span>
      <span class="name">Metallbau-Wasserkraft<br>Tessmar Lauber<br>GmbH &amp; Co. KG</span>
    </div>
    <nav class="nav">
      <a href="#">Über uns</a><a href="#">Stahlwasserbau</a><a href="#">Rechenreiniger</a><a href="#">Weitere Stahlbau-Produkte</a><a href="#">Neuigkeiten</a>
    </nav>
  </header>

  <section class="abs hero" role="img" aria-label="Foto einer Wehranlage aus Stahl mit grünem Steg über einem Fluss">
    <h1>STAHLWASSERBAU<br>MIT TRADITION UND INNOVATION</h1>
  </section>
  <svg class="abs hero-wave" width="1219" height="70" viewBox="0 0 1219 70" preserveAspectRatio="none">
    <path d="M0 30 C200 10 380 60 620 55 C820 50 1000 10 1219 20 L1219 70 L0 70Z" fill="#0b6ea5"/>
    <path d="M0 45 C220 20 400 65 620 62 C830 58 1010 25 1219 32 L1219 70 L0 70Z" fill="#e1f3fb"/>
  </svg>

  <section class="abs intro">
    <h2 class="h2" style="top:55px">METALLBAU WASSERKRAFT TESSMAR LAUBER</h2>
    <p class="lead">Ihr Partner für Metallbau und Stahlwasserbau in Brunnwalde bei Eschenfels</p>
    <div class="copy">
      <p>Metallbau Wasserkraft Tessmar Lauber – ein Name, der in ganz Deutschland für qualitativ hochwertigen Stahlwasser- und Metallbau, fachgerechte Montage und umfassenden Kundenservice steht. Als erfahrener Fachbetrieb in Brunnwalde bei Eschenfels fertigen und montieren wir verschiedenste Produkte aus folgenden Bereichen:</p>
      <ul class="ticks">
        <li><svg width="17" height="12" viewBox="0 0 17 12" fill="none" stroke="#0a7db5" stroke-width="1.5"><path d="M1 7l3 3 6-9M7 9l1.5 1.5L16 1"/></svg>allgemeiner Stahlbau</li>
        <li><svg width="17" height="12" viewBox="0 0 17 12" fill="none" stroke="#0a7db5" stroke-width="1.5"><path d="M1 7l3 3 6-9M7 9l1.5 1.5L16 1"/></svg>Geländerbau nach GEL-Vorschriften</li>
        <li><svg width="17" height="12" viewBox="0 0 17 12" fill="none" stroke="#0a7db5" stroke-width="1.5"><path d="M1 7l3 3 6-9M7 9l1.5 1.5L16 1"/></svg>Bau von Tor- und Treppenanlagen</li>
      </ul>
      <p>Auf den folgenden Seiten erfahren Sie mehr über unser Unter-<br>nehmen und unser Produktportfolio. Natürlich wissen wir um die Vorteile persönlicher Beratung und legen Wert auf eine individuelle Kundenbetreuung. Gern laden wir Sie in unsere Geschäftsräume nahe Eschenfels zu einem persönlichen Gespräch ein.</p>
    </div>
    <a class="btn call" href="#">
      <svg width="22" height="22" viewBox="0 0 24 24" fill="none" stroke="#fff" stroke-width="1.4"><path d="M5 3h4l2 5-2.5 1.5a11 11 0 0 0 6 6L16 13l5 2v4a2 2 0 0 1-2 2A16 16 0 0 1 3 5a2 2 0 0 1 2-2z"/></svg>03746 558310</a>
    <a class="btn send" href="#">
      <svg width="22" height="17" viewBox="0 0 24 18" fill="none" stroke="#fff" stroke-width="1.4"><rect x="1" y="1" width="22" height="16" rx="3"/><path d="M2 3l10 7 10-7"/></svg>Email senden</a>
    <div class="photo-building" role="img" aria-label="Foto des gelben Firmengebäudes mit Firmenfahrzeugen davor"></div>
  </section>

  <svg class="abs" style="left:0;top:1150px;z-index:2" width="1219" height="50" viewBox="0 0 1219 50" preserveAspectRatio="none">
    <path d="M0 28 C250 5 420 10 640 42 C850 50 1050 20 1219 10 L1219 50 L0 50Z" fill="#fff"/>
  </svg>

  <section class="abs products">
    <h2 class="h2" style="top:75px">UNSERE PRODUKTE &amp; LEISTUNGEN</h2>
    <div class="card" style="left:191px">
      <div class="badge"><svg width="44" height="36" viewBox="0 0 44 36" fill="none" stroke="#fff" stroke-width="3" stroke-linecap="round"><path d="M3 6q4.5-4 9.5 0t9.5 0 9.5 0 9.5 0M3 15q4.5-4 9.5 0t9.5 0 9.5 0 9.5 0M3 24q4.5-4 9.5 0t9.5 0 9.5 0 9.5 0M3 33q4.5-4 9.5 0t9.5 0 9.5 0 9.5 0"/></svg></div>
      <h3>Stahlwasserbau</h3>
      <ul><li>Schützanlagen</li><li>Dammtafeln</li><li>Wehrklappen</li><li>Fischaufstiegshilfen</li><li>Rechenanlagen</li><li>Schwimmbalken</li><li>Hochwasserschutztore</li></ul>
    </div>
    <div class="card" style="left:477px">
      <div class="badge"><svg width="44" height="44" viewBox="0 0 44 44" fill="none" stroke="#fff" stroke-width="3" stroke-linejoin="round"><path d="M24 4l6 4-5 10 7 6-9 16H8q2-8 2-14l8-6z"/><path d="M14 26l14 10M18 40l4-8M13 40l4-8"/></svg></div>
      <h3>Rechenreiniger</h3>
      <ul><li>Stangenreiniger</li><li>Horizontal-Rechenreiniger</li><li>Knickarmreiniger</li></ul>
    </div>
    <div class="card" style="left:763px">
      <div class="badge"><svg width="42" height="40" viewBox="0 0 42 40" fill="none" stroke="#fff" stroke-width="3" stroke-linejoin="round"><path d="M3 37h36V4a2 2 0 0 0-2-2H27v13H15v12H5a2 2 0 0 0-2 2z"/></svg></div>
      <h3>Stahlbau</h3>
      <ul><li>Treppen &amp; Stege</li><li>Geländer</li></ul>
    </div>
  </section>

  <svg class="abs" style="left:0;top:1770px;z-index:2" width="1219" height="50" viewBox="0 0 1219 50" preserveAspectRatio="none">
    <path d="M0 20 C200 5 420 8 620 32 C850 40 1050 5 1219 2 L1219 50 L0 50Z" fill="#e1f3fb"/>
  </svg>

  <section class="abs news">
    <h2 class="h2" style="top:62px">NEUIGKEITEN</h2>
    <article class="post" style="left:191px">
      <div class="pic" role="img" aria-label="Foto einer Schützanlage auf einer Baustelle" style="background:linear-gradient(160deg,#b9b5ac,#8e8c86 60%,#a49c8c)"></div>
      <p class="date">25.Juni 2024</p>
      <h4>Ein kleines Bächlein namens Duden fließt durch ihren Ort</h4>
      <p>Nicht einmal von der allmächtigen Inter-<br>punktion werden die Blindtexte beherrscht – ein geradezu unorthographisches Leben…</p>
    </article>
    <article class="post" style="left:477px">
      <div class="pic" role="img" aria-label="Luftbild eines Firmengeländes im Grünen" style="background:linear-gradient(160deg,#4f6d3a,#6e7f56 45%,#c9b98c 70%,#5d7844)"></div>
      <p class="date">25.Juni 2024</p>
      <h4>Ein kleines Bächlein namens Duden fließt durch ihren Ort</h4>
      <p>Nicht einmal von der allmächtigen Inter-<br>punktion werden die Blindtexte beherrscht – ein geradezu unorthographisches Leben…</p>
    </article>
    <article class="post" style="left:763px">
      <div class="pic" role="img" aria-label="Foto einer Fischaufstiegsanlage mit Weg und Wiese" style="background:linear-gradient(160deg,#5c7a3f,#8ea06a 40%,#b8b6a8 70%,#7d8a66)"></div>
      <p class="date">25.Juni 2024</p>
      <h4>Ein kleines Bächlein namens Duden fließt durch ihren Ort</h4>
      <p>Nicht einmal von der allmächtigen Inter-<br>punktion werden die Blindtexte beherrscht – ein geradezu unorthographisches Leben…</p>
    </article>
    <a class="more" href="#">Alle Neuigkeiten</a>
  </section>

  <svg class="abs" style="left:0;top:2370px;z-index:2" width="1219" height="40" viewBox="0 0 1219 40" preserveAspectRatio="none">
    <path d="M0 14 C250 4 450 18 620 12 C850 4 1050 18 1219 10 L1219 40 L0 40Z" fill="#0a7db5"/>
  </svg>

  <footer class="abs footer">
    <div class="col" style="left:192px">
      <svg width="20" height="24" viewBox="0 0 20 24" fill="none" stroke="#fff" stroke-width="1.4"><path d="M10 23s8-8 8-13a8 8 0 0 0-16 0c0 5 8 13 8 13z"/><circle cx="10" cy="10" r="3"/></svg>
      Metallbau-Wasserkraft Tessmar Lauber GmbH &amp; Co. KG<br>Am Erlengrund 7 | 08471 Brunnwalde
    </div>
    <div class="col" style="left:619px">
      <svg width="22" height="22" viewBox="0 0 24 24" fill="none" stroke="#fff" stroke-width="1.4"><path d="M5 3h4l2 5-2.5 1.5a11 11 0 0 0 6 6L16 13l5 2v4a2 2 0 0 1-2 2A16 16 0 0 1 3 5a2 2 0 0 1 2-2z"/></svg>
      Telefon: 03746 558310<br>Telefax: 03746 558311
    </div>
    <div class="col" style="left:834px">
      <svg width="24" height="20" viewBox="0 0 24 18" fill="none" stroke="#fff" stroke-width="1.4"><rect x="1" y="1" width="22" height="16" rx="3"/><path d="M2 3l10 7 10-7"/></svg>
      info@metallbau-tessmar-lauber-beispiel.de<br>Kontaktformular
    </div>
  </footer>

  <div class="abs bottombar">
    <nav><a href="#">Kontakt</a><a href="#">Anfahrt</a><a href="#">Partner</a><a href="#">Impressum</a><a href="#">Datenschutz</a><a href="#">Sitemap</a></nav>
  </div>

</div>
</body>
</html>
```